Shopguidance.net

I've attached two different logo's which I both like and would like to see different designs with each logo. I'm starting a retail consulting business and blog. You can view the start of my project at shopguidance.net to get an idea of what I'm creating.
Looking for a design that says creative, strategic and community.
Updates
Hello Everyone,
Thank you for the amazing design so far.
What I Like
- double sided designs, front and back
- one side should be white or green. Customers cannot write on or make notes on an all black card
- Simple, cool, creative is best
My business card will only have the following
- Instagram
- Facebook
- Email
- Website
My new Tag line is
Think Smart. Lead Smart. Work Smart.
My title will be:
Tobin Marlowe
Retail Consultant
Please submit 1 or 2 designs with these specifications.
Thank you,
Tobin
Reason: Looking for a few more designs and have now committed the project and it is no longer refundable. Please read brief and follow specific instructions.
Looking for something simple yet creative. Something that may stand out from most cards.
Thank you,
Tobin
Thank you,
Tobin
Target Market(s)
My main target is retail managers and retail businesses that are focused on leadership and people development.
Industry/Entity Type
Retail
Look and feel
Each slider illustrates characteristics of the customer's brand and the style your logo design should communicate.

```html
<!DOCTYPE html>
<html lang="en">
<head>
<meta charset="utf-8">
<title>Shopguidance business card</title>
<link rel="stylesheet" href="https://fonts.googleapis.com/css2?family=Open+Sans:wght@400;600;700&display=swap">
<style>
  :root {
    --bg: #e6e6e4;
    --card-dark: #1d1a1a;
    --card-light: #ffffff;
    --ink: #1e1e1e;
    --ink-soft: #3a3a3a;
    --green: #3fa535;
    --green-light: #6cc04a;
    --stripe: #2f2f2f;
    --muted: #bdbdbd;
  }
  * { margin: 0; padding: 0; box-sizing: border-box; }
  html, body { width: 1200px; height: 871px; overflow: hidden; }
  body {
    background: var(--bg);
    font-family: "Open Sans", Arial, sans-serif;
    display: flex;
    align-items: center;
    justify-content: center;
    gap: 48px;
  }
  .card {
    width: 520px;
    height: 300px;
    position: relative;
    overflow: hidden;
    box-shadow: 0 6px 18px rgba(0,0,0,0.18);
  }
  .card--back {
    background: var(--card-dark);
    display: flex;
    flex-direction: column;
    align-items: center;
    justify-content: center;
    gap: 14px;
  }
  .brand {
    display: flex;
    align-items: center;
    gap: 12px;
  }
  .brand__dot {
    width: 36px;
    height: 36px;
    border-radius: 50%;
    background: var(--green);
  }
  .brand__name {
    font-weight: 600;
    font-size: 34px;
    letter-spacing: -0.5px;
    color: var(--green-light);
  }
  .tagline {
    font-size: 12px;
    letter-spacing: 1px;
    color: var(--muted);
  }
  .card--front { background: var(--card-light); }
  .contact {
    position: absolute;
    left: 40px;
    top: 40px;
    color: var(--ink-soft);
  }
  .contact__name {
    font-weight: 700;
    font-size: 15px;
    color: var(--ink);
    letter-spacing: 0.3px;
  }
  .contact__title {
    font-size: 11px;
    color: var(--green);
    margin-bottom: 20px;
  }
  .contact__list { list-style: none; }
  .contact__item {
    display: flex;
    align-items: center;
    gap: 14px;
    font-size: 11px;
    line-height: 1;
    margin-bottom: 10px;
  }
  .contact__icon { width: 11px; height: 11px; flex: none; }
  .contact__mark {
    width: 10px;
    height: 10px;
    flex: none;
    background: var(--green);
  }
  .contact__mark--round { border-radius: 50%; }
  .card--front .brand {
    position: absolute;
    right: 36px;
    top: 112px;
  }
  .card--front .brand__name { color: var(--green); font-size: 30px; }
  .card--front .brand__dot { width: 32px; height: 32px; }
  .swoosh {
    position: absolute;
    left: 0;
    bottom: 0;
    width: 520px;
    height: 300px;
  }
</style>
</head>
<body>
  <section class="card card--back">
    <div class="brand">
      <span class="brand__dot"></span>
      <span class="brand__name">Shopguidance</span>
    </div>
    <p class="tagline">Think Smart. Lead Smart. Work Smart.</p>
  </section>

  <section class="card card--front">
    <svg class="swoosh" viewBox="0 0 520 300" aria-hidden="true">
      <defs>
        <linearGradient id="band" x1="0" y1="0" x2="1" y2="0">
          <stop offset="0" stop-color="#5bb83f"/>
          <stop offset="1" stop-color="#3a9a2e"/>
        </linearGradient>
      </defs>
      <path d="M0,226 C130,258 330,262 520,232 L520,300 L0,300 Z" fill="url(#band)"/>
      <path d="M0,246 C150,266 300,300 400,300 L0,300 Z" fill="#ffffff"/>
      <path d="M0,222 C130,254 330,258 520,228" fill="none" stroke="var(--stripe)" stroke-width="5"/>
    </svg>

    <div class="contact">
      <p class="contact__name">Tobin Marlowe</p>
      <p class="contact__title">Retail Consultant</p>
      <ul class="contact__list">
        <li class="contact__item">
          <span class="contact__mark contact__mark--round"></span>
          @shopguidance
        </li>
        <li class="contact__item">
          <span class="contact__mark"></span>
          /shopguidance
        </li>
        <li class="contact__item">
          <svg class="contact__icon" viewBox="0 0 12 12" aria-hidden="true"><rect x="0.5" y="2" width="11" height="8" fill="none" stroke="var(--green)"/><path d="M0.5 2l5.5 4.5 5.5-4.5" fill="none" stroke="var(--green)"/></svg>
          tobin@shopguidance.net
        </li>
        <li class="contact__item">
          <svg class="contact__icon" viewBox="0 0 12 12" aria-hidden="true"><circle cx="6" cy="6" r="5.2" fill="none" stroke="var(--green)"/><ellipse cx="6" cy="6" rx="2.2" ry="5.2" fill="none" stroke="var(--green)"/><path d="M1 6h10" stroke="var(--green)"/></svg>
          www.shopguidance.net
        </li>
      </ul>
    </div>

    <div class="brand">
      <span class="brand__dot"></span>
      <span class="brand__name">Shopguidance</span>
    </div>
  </section>
</body>
</html>
```